Packing for Razor Blade VELKORN

Dears: We need a packing design. The product is an Disposable Razor Blade. We are a company in Brazil.

The packing consists in a bag package which the Disposables Razos are placed. 5 units into each bag.

The bag is not 100% printed and should let a space to the customer see the razors inside. Some competitors uses oval circle. I attached competitor package (Dov Harborline)

The background color should be blue, this color tonality should vary its magnitude from dark blue to soft blue. Blue is a good color for personal care products because customer can take the impression of cleanness, especially for razor blade which has the fuction to shave.

You can feel free to add other colors however it can not be much colorfull because it may get trouble to printer company print it. Silver is good.

You can feel free to do details. You can feel free also to place the logo above the package or at bottom of it.

Dimmensions:
Heigh 24cm
Width 10cm

Featuring
- Featuring: Handle with Grip. In Portuguese - (Cabo Aderente)
- Featuring: 2 Razors. In portuguese - (Duas Lâminas)

Reason: I stayed many days with out providing feedbacks. I want to give more time for you .

Target Market(s)

Mans ( for woman we will design other package )

Requirements
Nice to have
• maybe some tears as a wet surface...
pls can feel free

```html
<!DOCTYPE html>
<html lang="en">
<head>
<meta charset="utf-8">
<title>VELKORN Disposable Razor Pack</title>
<link href="https://fonts.googleapis.com/css2?family=Orbitron:wght@700;900&display=swap" rel="stylesheet">
<style>
  :root {
    --stage: #d7d8de;
    --pack-top: #a4b4f6;
    --pack-mid: #9aabf1;
    --pack-low: #8797dc;
    --pack-foot: #a9b7ef;
    --navy: #0b1238;
    --band: #050b2a;
    --ring: #ffffff;
    --window-a: #c9d2f6;
    --window-b: #3c4f9a;
    --orbit-glow: rgba(235,240,255,0.35);
    --logo: #ffffff;
  }
  * { margin: 0; padding: 0; box-sizing: border-box; }
  html, body { width: 1200px; height: 1200px; overflow: hidden; background: var(--stage); }
  .canvas { position: relative; width: 1200px; height: 1200px; }
  .pack {
    position: absolute; left: 370px; top: 48px; width: 460px; height: 1104px;
    overflow: hidden;
    background: linear-gradient(180deg, var(--pack-top) 0%, var(--pack-mid) 55%, var(--pack-low) 84%, var(--pack-foot) 100%);
  }
  .orbit-art {
    position: absolute; left: 0; top: 110px; width: 460px; height: 700px;
    background: radial-gradient(ellipse 60% 50% at 50% 45%, var(--orbit-glow), rgba(235,240,255,0) 70%);
  }
  .orbit-art-low {
    position: absolute; left: 0; top: 1040px; width: 460px; height: 64px;
    background: radial-gradient(ellipse 70% 100% at 50% 100%, var(--orbit-glow), rgba(235,240,255,0) 80%);
  }
  .window-product { position: absolute; left: 0; top: 0; }
  .feature-copy {
    position: absolute; left: 0; right: 0; top: 752px;
    font-family: "Orbitron", sans-serif; font-weight: 900; color: var(--navy);
    font-style: italic; text-transform: uppercase; letter-spacing: 1px;
    font-size: 30px; line-height: 54px;
  }
  .feature-copy .feature { display: block; white-space: nowrap; }
  .feature-grip { padding-left: 28px; }
  .feature-blades { padding-left: 92px; }
  .feather-art {
    position: absolute; left: 80px; top: 850px; width: 150px; height: 76px;
    border-radius: 50%;
    background: radial-gradient(ellipse at 45% 50%, rgba(255,230,245,0.85), rgba(190,220,255,0.5) 55%, rgba(160,180,240,0) 75%);
    transform: rotate(-12deg);
  }
  .brand-band {
    position: absolute; left: 0; right: 0; top: 955px; height: 85px;
    background: var(--band);
    display: flex; align-items: center; justify-content: center; gap: 12px;
    padding-right: 20px;
  }
  .brand-mark { width: 12px; height: 12px; border-radius: 50%; background: var(--logo); }
  .brand-name {
    font-family: "Orbitron", sans-serif; font-weight: 700; color: var(--logo);
    font-size: 24px; letter-spacing: 1px;
  }
</style>
</head>
<body>
<main class="canvas">
  <section class="pack">
    <div class="orbit-art" role="img" aria-label="Decorative dashed orbit lines circling the window"></div>
    <div class="orbit-art-low" role="img" aria-label="Decorative dashed orbit lines near the pack base"></div>
    <svg class="window-product" width="460" height="1104" viewBox="0 0 460 1104">
      <defs>
        <linearGradient id="windowFill" x1="0" y1="0" x2="0" y2="1">
          <stop offset="0" stop-color="var(--window-a)"/>
          <stop offset="1" stop-color="var(--window-b)"/>
        </linearGradient>
      </defs>
      <ellipse cx="225" cy="392" rx="168" ry="246" transform="rotate(14 225 392)" fill="var(--ring)"/>
      <ellipse cx="235" cy="384" rx="126" ry="208" transform="rotate(14 235 384)" fill="url(#windowFill)"
               role="img" aria-label="Clear window showing two blue disposable razors inside the pack"/>
    </svg>
    <div class="feature-copy">
      <span class="feature feature-grip">Handle with grip</span>
      <span class="feature feature-blades">2 Razors</span>
    </div>
    <div class="feather-art" role="img" aria-label="Soft pastel feather illustration"></div>
    <div class="brand-band">
      <span class="brand-mark"></span>
      <span class="brand-name">VELKORN</span>
    </div>
  </section>
</main>
</body>
</html>
```